Dyrano In-home Personal Training

I would like to have some eye-catching business card design. Opened to any ideas.

The business idea: mobile fitness - train clients at their places

Target Market(s)

General population, 20-60 years old

Industry/Entity Type

Fitness

Contact Information for Business Card

The information to include:
Name: Marta
Call or text: 306-555-0187
Website: Dyrano.ca
Please use the attached logo

Requirements
Should not have
• No orange or purple colours please

```html
<!DOCTYPE html>
<html lang="en">
<head>
<meta charset="utf-8">
<title>Dyrano – Business Card</title>
<link rel="stylesheet" href="https://fonts.googleapis.com/css2?family=Arimo:wght@400;700&display=swap">
<style>
  :root {
    --page-bg: #e6e6e6;
    --card-bg: #414143;
    --card-text: #ffffff;
    --disc-light: #f6f6f6;
    --disc-mid: #e4e2e2;
    --brand-ink: #2f2f31;
  }
  * { margin: 0; padding: 0; box-sizing: border-box; }
  html, body {
    width: 1200px;
    height: 900px;
    overflow: hidden;
    background: var(--page-bg);
  }
  .canvas {
    position: relative;
    width: 1200px;
    height: 900px;
  }
  .business-card {
    position: absolute;
    left: 75px;
    top: 125px;
    width: 1050px;
    height: 650px;
    background: var(--card-bg);
    color: var(--card-text);
    font-family: "Arimo", Arial, sans-serif;
    box-shadow: 0 18px 40px rgba(0,0,0,0.18);
    overflow: hidden;
  }
  .holder-name {
    position: absolute;
    left: 53px;
    top: 84px;
    font-size: 40px;
    font-weight: 700;
    letter-spacing: 0.5px;
  }
  .contact-list {
    position: absolute;
    left: 50px;
    top: 202px;
    list-style: none;
  }
  .contact-item {
    display: flex;
    align-items: center;
    gap: 8px;
    font-size: 35px;
    height: 40px;
    margin-bottom: 28px;
  }
  .contact-icon { width: 36px; height: 36px; flex: none; }
  .service-list {
    position: absolute;
    left: 44px;
    top: 470px;
    list-style: none;
  }
  .service-item {
    display: flex;
    align-items: center;
    font-size: 33px;
    height: 40px;
    margin-bottom: 17px;
  }
  .service-item::before {
    content: "";
    width: 15px;
    height: 15px;
    border-radius: 50%;
    background: var(--card-text);
    margin-right: 6px;
    flex: none;
  }
  .brand-disc {
    position: absolute;
    left: 431px;
    top: 40px;
    width: 564px;
    height: 564px;
    border-radius: 50%;
    background: radial-gradient(circle at 45% 40%, var(--disc-light), var(--disc-mid));
    display: flex;
    flex-direction: column;
    align-items: center;
    justify-content: center;
    padding-top: 40px;
    font-family: "Arimo", Arial, sans-serif;
    font-weight: 400;
    color: var(--brand-ink);
    text-align: center;
  }
  .brand-name {
    font-size: 80px;
    line-height: 1;
  }
  .brand-tagline {
    margin-top: 18px;
    font-size: 22px;
    line-height: 1.2;
  }
</style>
</head>
<body>
<main class="canvas">
  <section class="business-card">
    <h1 class="holder-name">MARTA</h1>

    <ul class="contact-list">
      <li class="contact-item">
        <svg class="contact-icon" viewBox="0 0 36 36" aria-hidden="true">
          <rect x="3" y="3" width="30" height="30" rx="5" fill="none" stroke="#fff" stroke-width="2.6"/>
          <path d="M12 9c1.5 0 2.5 3.5 2.5 4.5s-2 1.5-1.5 3 3.5 5 5 5.5 2-1.5 3-1.5 4.5 1 4.5 2.5-1.5 3.5-3.5 3.5C15 26.5 9.5 21 9.5 13c0-2 1-4 2.5-4z" fill="#fff"/>
        </svg>
        <span>306-555-0187</span>
      </li>
      <li class="contact-item">
        <svg class="contact-icon" viewBox="0 0 36 36" aria-hidden="true">
          <g fill="none" stroke="#fff" stroke-width="2.4">
            <circle cx="18" cy="18" r="14"/>
            <ellipse cx="18" cy="18" rx="6" ry="14"/>
            <line x1="4" y1="18" x2="32" y2="18"/>
            <path d="M7 10.5h22M7 25.5h22"/>
          </g>
        </svg>
        <span>www.Dyrano.ca</span>
      </li>
    </ul>

    <ul class="service-list">
      <li class="service-item">Mobile Fitness</li>
      <li class="service-item">Train clients at their places</li>
    </ul>

    <div class="brand-disc">
      <div class="brand-name">Dyrano</div>
      <div class="brand-tagline">In-home Personal Training</div>
    </div>
  </section>
</main>
</body>
</html>
```